Lorvena Aesthetic Doctor

I require an elegant, luxurious looking business card for my aesthetic business. I am a doctor and that will set me aside from competitors. I am planning to provide home and spa based treatments to clients with high expectations. I have attached my logo.

```html
<!DOCTYPE html>
<html lang="en">
<head>
<meta charset="utf-8">
<title>Lorvena Aesthetic Doctor – Business Card</title>
<link href="https://fonts.googleapis.com/css2?family=Roboto:wght@300;400;500;700&display=swap" rel="stylesheet">
<style>
  :root {
    --bg: #e9ebee;
    --blue-top: #3eaae6;
    --blue-bottom: #1e6dc2;
    --sky: #58b8e6;
    --pale-sky: #bfe3f7;
    --grey-text: #8a8d91;
    --grey-line: #a9acb0;
    --white: #ffffff;
    --shadow: rgba(30, 40, 60, 0.18);
  }
  * { box-sizing: border-box; margin: 0; padding: 0; }
  html, body {
    width: 1200px; height: 1200px; overflow: hidden;
    background: var(--bg);
    font-family: "Roboto", Arial, sans-serif;
  }
  .canvas {
    width: 1200px; height: 1200px;
    display: flex; flex-direction: column; align-items: center; justify-content: center;
    gap: 48px;
  }
  .card {
    position: relative;
    width: 860px; height: 526px;
    border-radius: 4px;
    box-shadow: 0 10px 30px var(--shadow);
    overflow: hidden;
  }

  /* Front side */
  .card-front {
    background: linear-gradient(170deg, var(--blue-top) 0%, #2f8ad6 55%, var(--blue-bottom) 100%);
    color: var(--white);
  }
  .front-ring {
    position: absolute; right: -40px; top: 60px;
    width: 460px; height: 460px; border-radius: 50%;
    border: 10px solid rgba(255,255,255,0.12);
  }
  .front-brand {
    position: absolute; left: 0; right: 0; top: 150px;
    display: flex; align-items: center; justify-content: center; gap: 22px;
  }
  .brand-dot {
    width: 70px; height: 70px; border-radius: 50%;
    border: 3px solid var(--white);
  }
  .brand-name {
    font-weight: 300; font-size: 52px; letter-spacing: 5px;
    text-transform: uppercase; color: var(--white); line-height: 1;
  }
  .brand-name small { display: block; font-size: 24px; letter-spacing: 6px; margin-top: 10px; }
  .services {
    position: absolute; left: 0; right: 0; top: 300px;
    text-align: center; font-weight: 400; font-size: 26px; line-height: 1.5;
    letter-spacing: 0.5px;
  }

  /* Back side */
  .card-back { background: var(--white); }
  .back-brand {
    position: absolute; left: 70px; top: 130px;
    width: 260px; height: 260px;
    display: flex; align-items: center; justify-content: center;
  }
  .back-ring {
    position: absolute; inset: 0; border-radius: 50%;
    border: 5px solid var(--grey-line);
  }
  .back-name {
    position: relative; font-weight: 400; font-size: 38px;
    letter-spacing: 3px; text-transform: uppercase; color: var(--sky);
  }
  .divider {
    position: absolute; left: 380px; top: 110px;
    width: 2px; height: 270px; background: var(--grey-line);
  }
  .details { position: absolute; left: 420px; top: 115px; }
  .doctor {
    font-weight: 500; font-size: 34px; color: var(--sky);
  }
  .doctor .postnominals { font-size: 20px; font-weight: 500; margin-left: 6px; }
  .qualification {
    margin-top: 6px; font-weight: 400; font-size: 26px; line-height: 1.3;
    color: var(--grey-text);
  }
  .contacts { list-style: none; margin-top: 22px; }
  .contacts li {
    display: flex; align-items: center; gap: 16px;
    font-size: 26px; color: var(--grey-text); line-height: 1.55;
  }
  .contacts svg { width: 24px; height: 24px; flex: none; }
  .contacts .accent { color: var(--sky); }
  .social {
    position: absolute; left: 360px; top: 440px;
    display: flex; gap: 22px;
  }
  .social span {
    width: 34px; height: 34px; border-radius: 50%;
    background: var(--sky); display: block;
  }
</style>
</head>
<body>
<main class="canvas">

  <section class="card card-front" aria-label="Card front">
    <div class="front-ring" aria-hidden="true"></div>
    <div class="front-brand">
      <span class="brand-dot" aria-hidden="true"></span>
      <div class="brand-name">Lorvena<small>Aesthetic Doctor</small></div>
    </div>
    <p class="services">
      Dermal injectables • Plasma facials • Microneedling<br>
      Skin boosters • Excessive sweating<br>
      Home and Spa Based Treatments
    </p>
  </section>

  <section class="card card-back" aria-label="Card back">
    <div class="back-brand">
      <span class="back-ring" aria-hidden="true"></span>
      <span class="back-name">Lorvena</span>
    </div>
    <div class="divider" aria-hidden="true"></div>
    <div class="details">
      <h1 class="doctor">Dr Mirela Tansey,<span class="postnominals">MRCPCH MD</span></h1>
      <p class="qualification">Australasian Diploma<br>of Aesthetic Medicine</p>
      <ul class="contacts">
        <li>
          <svg viewBox="0 0 24 24" aria-hidden="true"><path d="M6.6 10.8a15.1 15.1 0 0 0 6.6 6.6l2.2-2.2c.3-.3.7-.4 1-.2 1.1.4 2.3.6 3.6.6.6 0 1 .4 1 1V20c0 .6-.4 1-1 1C10.6 21 3 13.4 3 4c0-.6.4-1 1-1h3.5c.6 0 1 .4 1 1 0 1.3.2 2.5.6 3.6.1.3 0 .7-.2 1L6.6 10.8z" fill="#58b8e6"/></svg>
          0800 555 017
        </li>
        <li>
          <svg viewBox="0 0 24 24" aria-hidden="true"><rect x="3" y="6" width="18" height="12" rx="1.5" fill="none" stroke="#58b8e6" stroke-width="1.8"/><path d="M3.5 7l8.5 6 8.5-6" fill="none" stroke="#58b8e6" stroke-width="1.8"/></svg>
          mirela@lorvena.co.nz
        </li>
        <li>
          <svg viewBox="0 0 24 24" aria-hidden="true"><g fill="none" stroke="#58b8e6" stroke-width="1.6"><circle cx="12" cy="12" r="9"/><ellipse cx="12" cy="12" rx="4" ry="9"/><path d="M3 12h18M5 7h14M5 17h14"/></g></svg>
          <span>www.<span class="accent">lorvena</span>.co.nz</span>
        </li>
      </ul>
    </div>
    <div class="social" aria-hidden="true"><span></span><span></span></div>
  </section>

</main>
</body>
</html>
```